Design some Stationery for Legal Practice

I want to design my stationery for my legal practice. Logo is provided.
I want creative, modern, simple and clean...maybe unusual.
I need letterheads, envelopes, and business cards designed.
Must deliver designs in different formats.

Contestant must use sample data. REAL DATA WILL BE PROVIDED TO WINNER.

If more info is needed, please don't hesitate to ask.

```html
<!DOCTYPE html>
<html lang="en">
<head>
<meta charset="utf-8">
<title>Quillmere Law — Envelope Set</title>
<link rel="stylesheet" href="https://fonts.googleapis.com/css2?family=Montserrat:wght@300;400&display=swap">
<style>
  :root {
    --backdrop: #3a3a3a;
    --paper: #ffffff;
    --charcoal: #3b3b3b;
    --ink: #4a4a4a;
    --orange: #f4a11f;
    --muted: #8a8a8a;
    --fold: #ececec;
    --band-text: #e6e6e6;
  }
  * { margin: 0; padding: 0; box-sizing: border-box; }
  html, body { width: 1200px; height: 899px; overflow: hidden; }
  body {
    background: var(--backdrop);
    font-family: "Montserrat", sans-serif;
    position: relative;
  }
  .envelope {
    position: absolute;
    width: 520px;
    height: 260px;
    background: var(--paper);
    box-shadow: 0 18px 40px rgba(0,0,0,0.45);
    overflow: hidden;
  }
  .envelope svg { position: absolute; inset: 0; }
  .envelope-front { left: 50px; top: 320px; }
  .envelope-back { left: 630px; top: 320px; }

  .wordmark {
    position: absolute;
    font-weight: 400;
    font-size: 24px;
    letter-spacing: 2px;
    color: var(--ink);
    text-transform: uppercase;
    white-space: nowrap;
  }
  .envelope-front .wordmark { left: 24px; top: 20px; }
  .envelope-back .wordmark {
    left: 0; right: 0; top: 92px; text-align: center;
    color: var(--charcoal);
  }
  .tagline {
    position: absolute;
    left: 25px; top: 53px;
    font-size: 8px;
    font-weight: 300;
    color: var(--muted);
    letter-spacing: 0.3px;
    white-space: nowrap;
  }
  .web-address {
    position: absolute;
    left: 20px; bottom: 5px;
    font-size: 11px;
    letter-spacing: 2px;
    color: var(--band-text);
    font-weight: 400;
    white-space: nowrap;
  }
</style>
</head>
<body>

  <section class="envelope envelope-front" aria-label="Envelope front">
    <svg width="520" height="260" viewBox="0 0 520 260" aria-hidden="true">
      <path class="front-band" d="M0 228 H112 Q118 228 122 234 L126 240 H520 V260 H0 Z" fill="var(--charcoal)"/>
      <path class="front-accent" d="M112 228 Q118 228 122 234 L126 240 H520 V236 H128 L125 231 Q120 224 112 224 H0 V228 Z" fill="var(--orange)"/>
    </svg>
    <div class="wordmark">Quillmere Law</div>
    <div class="tagline">Clear Counsel for Every Step Ahead</div>
    <div class="web-address">www.quillmerelaw.com</div>
  </section>

  <section class="envelope envelope-back" aria-label="Envelope back">
    <svg width="520" height="260" viewBox="0 0 520 260" aria-hidden="true">
      <path class="back-flap" d="M0 0 H520 V70 Q500 110 470 112 Q360 112 260 150 Q160 112 50 112 Q20 110 0 70 Z" fill="var(--orange)"/>
      <path class="back-fold" d="M0 260 L260 150 L520 260" fill="none" stroke="var(--fold)" stroke-width="1.5"/>
    </svg>
    <div class="wordmark">Quillmere Law</div>
  </section>

</body>
</html>
```